UK vitamin company needs a packaging label design for new vitamin range

We have a logo, and we have the product. We now need some beautiful labels to go on the boxes which bring the product range to life.
We have 7 categories: Joint Care, Heart Heath, Brain Function, Immune System, Skin, Antioxidants and Probiotics. Each of these categories should have its own look within the plumble tonic range. This can be quite subtle, but needs to be clearly visible and should be linked to the category e.g. 'Heart Health' might have a heart etc.
I have uploaded the logo, an example of the pack shape, and the sizing info for the label.
We are a fun brand, so please have some fun with this. We want the labels to be bold, and differentiated from the rest of the category.
Thanks
All images used must be 'rights free'. Many thanks
UK
It Company

```html
<!DOCTYPE html>
<html lang="en">
<head>
<meta charset="utf-8">
<title>Plumble Tonic – Joint Care and Heart Heath labels</title>
<link href="https://fonts.googleapis.com/css2?family=Arimo:wght@700&family=Cabin:wght@500;600&family=Tinos:wght@400;700&display=swap" rel="stylesheet">
<style>
  :root {
    --canvas: #e6e6e6;
    --white: #ffffff;
    --green-deep: #2fa34a;
    --green-lime: #8cc63f;
    --green-pale: #cfe38a;
    --blue-deep: #1d4aa0;
    --blue-mid: #2f7fd0;
    --blue-pale: #cfe9f8;
    --joint-red: #a4383a;
    --heart-red: #e3262b;
    --navy: #0f2a4a;
    --ink: #222222;
    --brand-orange: #ea7420;
    --ring-grey: #d4d4d4;
  }
  * { box-sizing: border-box; margin: 0; padding: 0; }
  html, body { width: 1200px; height: 737px; overflow: hidden; background: var(--canvas); }
  .sheet { position: relative; width: 1200px; height: 737px; }

  .label { position: absolute; top: 20px; width: 548px; height: 696px; background: var(--white); overflow: hidden; }
  .label--joint { left: 18px; }
  .label--heart { left: 634px; }
  .label__art { position: absolute; inset: 0; width: 548px; height: 696px; }

  .brand-seal {
    position: absolute; top: 2px; left: 212px; width: 124px; height: 124px;
    border-radius: 50%; background: var(--white); border: 5px solid var(--ring-grey);
    display: flex; align-items: center; justify-content: center; text-align: center;
  }
  .brand-seal__name {
    font-family: "Cabin", sans-serif; font-weight: 600; font-size: 21px; line-height: 1.05;
    color: var(--brand-orange);
  }

  .joint-title {
    position: absolute; top: 178px; left: 0; width: 548px; text-align: center;
    font-family: "Cabin", sans-serif; font-weight: 500; font-size: 86px; color: var(--joint-red);
    letter-spacing: -1px; line-height: 1;
  }
  .joint-subtitle {
    position: absolute; top: 271px; left: 0; width: 548px; text-align: center;
    font-family: "Arimo", sans-serif; font-weight: 700; font-size: 16px; color: var(--ink);
  }
  .benefit {
    position: absolute; height: 32px; border-radius: 16px 0 0 16px;
    background: linear-gradient(90deg, #bfe3f7 0%, #e3f3fc 70%, rgba(255,255,255,0) 100%);
    font-family: "Tinos", serif; font-size: 19px; color: var(--ink);
    display: flex; align-items: center; padding-left: 24px;
  }
  .benefit--cartilage { top: 313px; left: 168px; width: 330px; }
  .benefit--strength { top: 368px; left: 198px; width: 300px; }
  .benefit--tablets { top: 422px; left: 234px; width: 310px; }

  .count-badge {
    position: absolute; width: 172px; height: 62px; border-radius: 50%;
    background: radial-gradient(ellipse at center, #e4f4fd 0%, #9fd3f1 100%);
    border: 3px solid #f4e9b6;
    display: flex; align-items: center; justify-content: center;
    font-family: "Tinos", serif; font-weight: 700; font-size: 26px; color: var(--navy);
  }
  .label--joint .count-badge { top: 498px; left: 350px; }
  .label--heart .count-badge { top: 498px; left: 344px; }

  .strength {
    position: absolute; top: 630px; font-family: "Tinos", serif; font-weight: 700; font-size: 27px; line-height: 1.2;
  }
  .label--joint .strength { left: 16px; color: var(--ink); }
  .label--heart .strength { left: 392px; color: var(--white); }

  .heart-title {
    position: absolute; left: 244px; font-family: "Tinos", serif; font-size: 100px; line-height: 1;
    color: var(--heart-red); transform: scaleX(0.82); transform-origin: left top; white-space: nowrap;
  }
  .heart-title--top { top: 198px; }
  .heart-title--bottom { top: 302px; }
</style>
</head>
<body>
<main class="sheet">

  <section class="label label--joint">
    <svg class="label__art" viewBox="0 0 548 696" aria-hidden="true">
      <defs>
        <linearGradient id="joint-top" x1="0" y1="0" x2="0" y2="1">
          <stop offset="0" stop-color="#2fa34a"/><stop offset="1" stop-color="#8cc63f"/>
        </linearGradient>
        <linearGradient id="joint-base" x1="0" y1="0" x2="1" y2="1">
          <stop offset="0" stop-color="#8cc63f"/><stop offset="1" stop-color="#d7e98f"/>
        </linearGradient>
      </defs>
      <path d="M0 0 H548 V112 C430 86 330 92 230 122 C140 146 60 140 0 124 Z" fill="url(#joint-top)"/>
      <path d="M0 124 C60 140 140 146 230 122 C330 92 430 86 548 112" fill="none" stroke="#d9d9d9" stroke-width="6"/>
      <path d="M0 300 C110 360 230 470 548 540 L548 696 L0 696 Z" fill="#e4f1c8"/>
      <path d="M0 330 C120 400 250 520 548 592 L548 696 L0 696 Z" fill="url(#joint-base)"/>
      <path d="M150 696 C260 640 400 630 548 640 L548 696 Z" fill="#c5df7c"/>
    </svg>

    <div class="brand-seal"><span class="brand-seal__name">plumble<br>tonic</span></div>

    <h1 class="joint-title">Joint Care</h1>
    <p class="joint-subtitle">Premium Strength to Support Healthy Joints</p>

    <p class="benefit benefit--cartilage">Normal function of cartilage</p>
    <p class="benefit benefit--strength">High strength formula</p>
    <p class="benefit benefit--tablets">Easy to take tablets</p>

    <svg class="label__art" viewBox="0 0 548 696">
      <defs>
        <radialGradient id="knee-glow" cx="0.45" cy="0.45" r="0.6">
          <stop offset="0" stop-color="#f08a2a"/><stop offset="1" stop-color="#0d3c8a"/>
        </radialGradient>
        <radialGradient id="shoulder-glow" cx="0.6" cy="0.4" r="0.6">
          <stop offset="0" stop-color="#c98a6a"/><stop offset="1" stop-color="#5a4aa0"/>
        </radialGradient>
        <radialGradient id="neck-glow" cx="0.4" cy="0.4" r="0.6">
          <stop offset="0" stop-color="#e23a3a"/><stop offset="1" stop-color="#2f63b8"/>
        </radialGradient>
      </defs>
      <circle cx="78" cy="388" r="70" fill="url(#knee-glow)" stroke="#d8eab0" stroke-width="5" role="img" aria-label="Glowing knee joint photo"/>
      <circle cx="164" cy="510" r="60" fill="url(#shoulder-glow)" stroke="#d8eab0" stroke-width="5" role="img" aria-label="Highlighted shoulder joint photo"/>
      <circle cx="276" cy="612" r="58" fill="url(#neck-glow)" stroke="#d8eab0" stroke-width="5" role="img" aria-label="Inflamed neck and shoulder photo"/>
    </svg>

    <p class="count-badge">60Tablets</p>
    <p class="strength">1500mg</p>
  </section>

  <section class="label label--heart">
    <svg class="label__art" viewBox="0 0 548 696">
      <defs>
        <linearGradient id="heart-top" x1="0" y1="0" x2="0" y2="1">
          <stop offset="0" stop-color="#1d4aa0"/><stop offset="1" stop-color="#2f7fd0"/>
        </linearGradient>
        <radialGradient id="anatomy" cx="0.4" cy="0.45" r="0.7">
          <stop offset="0" stop-color="#e8707a"/><stop offset="0.45" stop-color="#3b6fc0"/><stop offset="1" stop-color="#0c3a8a"/>
        </radialGradient>
        <linearGradient id="heart-corner" x1="0" y1="0" x2="1" y2="1">
          <stop offset="0" stop-color="#2f7fd0"/><stop offset="1" stop-color="#1d4aa0"/>
        </linearGradient>
      </defs>
      <path d="M0 0 H548 V112 C430 86 330 92 230 122 C140 146 60 140 0 124 Z" fill="url(#heart-top)" aria-hidden="true"/>
      <path d="M0 124 C60 140 140 146 230 122 C330 92 430 86 548 112" fill="none" stroke="#d9d9d9" stroke-width="6" aria-hidden="true"/>
      <path d="M0 330 C160 330 360 380 548 450" fill="none" stroke="#e4f1c8" stroke-width="14" aria-hidden="true"/>
      <path d="M0 362 C160 350 360 390 548 470 L548 520 C440 560 360 620 320 696 L0 696 Z"
            fill="url(#anatomy)" role="img" aria-label="Translucent human heart and blood vessels photo"/>
      <path d="M320 696 C360 620 440 560 548 520" fill="none" stroke="#e4f1c8" stroke-width="8" aria-hidden="true"/>
      <path d="M352 696 L352 636 C420 628 480 624 548 620 L548 696 Z" fill="url(#heart-corner)" aria-hidden="true"/>

      <path transform="translate(0 58)" d="M98 302 C40 258 22 232 22 200 C22 168 46 146 76 146 C94 146 108 156 116 170 C124 156 138 146 156 146 C186 146 210 168 210 200 C210 232 192 258 134 302 L116 316 Z"
            fill="#d9232a" stroke="#3a2a2a" stroke-width="4" role="img" aria-label="Red heart icon"/>
      <polyline points="30,300 80,300 92,282 100,330 108,240 118,340 128,286 136,300 548,300"
                fill="none" stroke="#2a9de0" stroke-width="3" aria-hidden="true"/>
    </svg>

    <div class="brand-seal"><span class="brand-seal__name">plumble<br>tonic</span></div>

    <h1 class="heart-title heart-title--top">HEART</h1>
    <p class="heart-title heart-title--bottom">HEATH</p>

    <p class="count-badge">60Tablets</p>
    <p class="strength">1500mg</p>
  </section>

</main>
</body>
</html>
```